Flyer for Luxury Boarding Stable for Retired Horses

A one page flyer to hand out at stable tours and at horse shows. Willow Brook at 34 Meadows is a luxury equine boarding stable for retired horses. This is a new facility in Summerfield, NC that has 6 available stalls. We are trying to attract owners with 2 or more retired horses they would like to board.

Target Market(s)

Horse owners with 2 or more horses that are retired from showing, racing, or rodeo. These owners love their horses like family and want them well cared for in their retirement years.

Industry/Entity Type

Equestrian Boarding

Font styles to use
Script

Colors
EE7325
F08F49
F5BC92
FAE3D3
FDF4ED

Requirements
Must have
• Photos of the facility. Must feel upscale and worth the price.

```html
<!DOCTYPE html>
<html lang="en">
<head>
<meta charset="utf-8">
<title>Willow Brook at 34 Meadows – Retirement Boarding Flyer</title>
<link rel="stylesheet" href="https://fonts.googleapis.com/css2?family=Great+Vibes&family=Courgette&display=swap">
<style>
  :root{
    --page:#ffffff;
    --stone:#bdbcad;
    --sage:#abab84;
    --brown:#4b2513;
    --paper:#ffffff;
    --ink:#2a150b;
    --script:"Great Vibes", cursive;
    --body:"Courgette", cursive;
  }
  *{box-sizing:border-box;margin:0;padding:0}
  html,body{width:1200px;height:1000px;overflow:hidden;background:var(--page)}
  .flyer{position:absolute;left:324px;top:109px;width:552px;height:781px;background:var(--stone);overflow:hidden}
  .hero-photo{position:absolute;left:0;top:0;width:552px;height:276px;
    background:linear-gradient(160deg,#3f6b2a 0%,#6f8f4a 30%,#c9c5b6 50%,#8a8c84 62%,#5f8a3a 80%,#3d6a28 100%)}
  .panel{position:absolute;left:18px;top:218px;width:515px;height:544px;border-radius:14px;background:var(--sage)}
  .panel-fade{position:absolute;left:18px;top:218px;width:515px;height:58px;border-radius:14px 14px 0 0;
    background:linear-gradient(to bottom,rgba(171,171,132,.75),rgba(171,171,132,.95))}
  .title{position:absolute;left:38px;top:228px;width:230px;font-family:var(--script);color:var(--brown);
    font-size:56px;line-height:52px;font-weight:400}
  .aisle-photo{position:absolute;left:263px;top:236px;width:253px;height:164px;border:2px solid var(--brown);border-radius:8px;
    background:linear-gradient(to bottom,#7a4f22 0%,#b07a3a 35%,#9a7a52 55%,#8d8e8a 75%,#6d6e6a 100%)}
  .card{position:absolute;background:var(--paper);border:2px solid var(--brown);border-radius:6px;overflow:hidden}
  .intro{left:35px;top:411px;width:291px;height:119px}
  .intro-head{height:35px;background:var(--brown);color:#fff;font-family:var(--script);font-size:19px;
    display:flex;align-items:center;justify-content:center;white-space:nowrap}
  .intro p{padding:7px 8px;font-family:var(--body);font-size:10.4px;line-height:13.4px;color:var(--ink)}
  .contact{left:336px;top:411px;width:182px;height:120px}
  .contact p{height:82px;padding:7px 10px;font-family:var(--body);font-size:10.4px;line-height:13px;color:var(--ink)}
  .contact .phone{height:36px;background:var(--brown);color:#fff;font-family:var(--body);font-size:12.5px;
    display:flex;align-items:center;justify-content:center}
  .facilities{left:35px;top:540px;width:291px;height:207px;padding:4px 6px 0 10px}
  .facilities h2{font-family:var(--body);font-size:15px;text-align:center;color:var(--ink);font-weight:700;line-height:19px}
  .facilities ul{list-style:none}
  .facilities li{position:relative;padding-left:14px;font-family:var(--body);font-size:9.2px;line-height:12.6px;
    color:var(--ink);margin-bottom:5px}
  .facilities li::before{content:"";position:absolute;left:2px;top:4px;width:5px;height:5px;border-radius:50%;background:var(--ink)}
  .fees{left:336px;top:540px;width:182px;height:207px;background:transparent}
  .fees-head{height:42px;background:var(--brown);color:#fff;font-family:var(--body);font-size:19px;
    display:flex;align-items:center;justify-content:center}
  .fee{position:absolute;left:7px;width:165px;height:42px;background:var(--brown);color:#fff;font-family:var(--body);
    font-size:16px;display:flex;align-items:center;justify-content:center}
  .fee-1{top:51px}.fee-2{top:103px}.fee-3{top:154px}
</style>
</head>
<body>
<main class="flyer">
  <div class="hero-photo" role="img" aria-label="Aerial view of the barn, riding arena, drives and green pastures surrounded by trees"></div>
  <div class="panel"></div>
  <div class="panel-fade"></div>
  <h1 class="title">Willow Brook at 34 Meadows</h1>
  <div class="aisle-photo" role="img" aria-label="Interior barn aisle with wooden stalls and a concrete floor"></div>

  <section class="card intro">
    <div class="intro-head">Where Luxury Meets Equestrian Excellence</div>
    <p>Are you a devoted horse owner who believes in providing only the best for your equine companions? Look no further! Willow Brook at 34 Meadows offers a premier retirement horse boarding experience that combines opulence with top-tier care.</p>
  </section>

  <section class="card contact">
    <p>Contact us today to schedule a tour of Willow Brook at 34 Meadows. Meet Marisol, our friendly guide, who can be reached at:</p>
    <div class="phone">Call or Text: 555-014-2287</div>
  </section>

  <section class="card facilities">
    <h2>Facilities</h2>
    <ul>
      <li>Luxurious Stalls: Our six spacious stalls are meticulously designed, complete with back patios for your horse's comfort.</li>
      <li>Lush Pastures: Let your retired horses enjoy gentle exercise in our expansive, green pastures.</li>
      <li>World-Class Riding Arena: Ride like royalty under stadium lights in our state-of-the-art arena.</li>
      <li>Scenic Trails: Explore miles of picturesque trails across our 34-acre property.</li>
      <li>Quality Nutrition: We provide top-quality feed and hay to ensure your horse's well-being.</li>
      <li>Passionate Staff: Our experienced team is dedicated to providing loving care to your equine family members.</li>
    </ul>
  </section>

  <section class="card fees">
    <div class="fees-head">Boarding Fees:</div>
    <div class="fee fee-1">1st horse - $1,100/mo</div>
    <div class="fee fee-2">2nd horse - $900/mo</div>
    <div class="fee fee-3">3rd horse - $700/mo</div>
  </section>
</main>
</body>
</html>
```